Stationery design for pet company

We need a designer for stationery designs. The name of our company is Valtrix. We specialise in pet accessories as well as distribution of pet food. We also have a brand under us for our website called Brightwhiskerclub. We will need a letterhead for Valtrix and another for Brightwhiskerclub with matching envelopes. We also would like to have a business card design with name, contact details etc with the Valtrix logo on one side of the card. The other side of the business card should have the full logo of Brightwhiskerclub with our website www.brightwhiskerclub.com.

Target Market(s)

Stationery for Valtrix is for retail shops and suppliers, therefore should have a more professional feel. Stationery for Brightwhiskerclub is mainly for customers from the website.

Industry/Entity Type

Business

Requirements
Must have
• Preferably a use of black colour for the business card.
Nice to have
• Professional feel
Should not have
• Childish designs

```html
<!DOCTYPE html>
<html lang="en">
<head>
<meta charset="utf-8">
<title>Valtrix &amp; Brightwhiskerclub Stationery</title>
<link rel="stylesheet" href="https://fonts.googleapis.com/css2?family=Comic+Neue:wght@700&family=Michroma&family=Roboto+Mono:wght@700&display=swap">
<style>
  :root {
    --ink: #000000;
    --paper: #ffffff;
    --sun: #ffff00;
    --sky: #4dd2ff;
    --leaf: #33cc33;
    --rule: #555555;
    --mascot: #1a1a1a;
  }
  html, body {
    margin: 0;
    padding: 0;
    width: 1200px;
    height: 724px;
    overflow: hidden;
    background: var(--paper);
  }
  .canvas {
    position: relative;
    width: 1200px;
    height: 724px;
  }
  .card-front {
    position: absolute;
    left: 3px; top: 0;
    width: 634px; height: 350px;
    border: 2px solid var(--ink);
    background: var(--paper);
    box-sizing: border-box;
  }
  .web-tab {
    position: absolute;
    right: 1px; top: 2px;
    width: 282px; height: 85px;
    background: var(--sun);
    border: 2px solid var(--ink);
    box-sizing: border-box;
    display: flex; align-items: center; justify-content: center;
    font-family: "Roboto Mono", monospace;
    font-weight: 700;
    font-size: 15px;
    color: var(--ink);
  }
  .mascot {
    position: absolute;
    left: 242px; top: 102px;
    width: 140px; height: 134px;
    border-radius: 14px;
    background: radial-gradient(circle at 45% 45%, #3a3a3a, var(--mascot) 70%);
    box-shadow: 6px 6px 10px rgba(0,0,0,0.35);
  }
  .name-tab {
    position: absolute;
    left: 1px; bottom: 1px;
    width: 484px; height: 87px;
    background: var(--sky);
    border: 3px solid var(--ink);
    box-sizing: border-box;
    display: flex; align-items: center; padding-left: 22px;
    font-family: "Comic Neue", cursive;
    font-weight: 700;
    font-size: 46px;
    color: var(--ink);
  }
  .card-back {
    position: absolute;
    left: 3px; top: 371px;
    width: 634px; height: 351px;
    background: var(--ink);
    border: 1px solid var(--leaf);
    box-sizing: border-box;
    display: flex; align-items: center; justify-content: center;
  }
  .brand-mark {
    font-family: "Michroma", sans-serif;
    color: var(--leaf);
    letter-spacing: 0.12em;
    text-transform: uppercase;
  }
  .card-back .brand-mark { font-size: 56px; }
  .letterhead {
    position: absolute;
    left: 735px; top: 19px;
    width: 464px; height: 689px;
    border: 1px solid var(--rule);
    box-sizing: border-box;
    background: var(--paper);
  }
  .letterhead-address {
    position: absolute;
    left: 44px; top: 26px;
    width: 180px;
    text-align: center;
    font-family: "Michroma", sans-serif;
    font-size: 10px;
    line-height: 18px;
    font-variant: small-caps;
    letter-spacing: 0.06em;
    color: var(--ink);
  }
  .letterhead .brand-mark {
    position: absolute;
    left: 34px; top: 74px;
    width: 200px;
    text-align: center;
    font-size: 24px;
  }
</style>
</head>
<body>
<main class="canvas">
  <section class="card-front">
    <div class="web-tab">www.brightwhiskerclub.com</div>
    <div class="mascot" role="img" aria-label="Illustration of a cat and dog mascot pair"></div>
    <div class="name-tab">Brightwhiskerclub</div>
  </section>

  <section class="card-back">
    <div class="brand-mark">Valtrix</div>
  </section>

  <section class="letterhead">
    <address class="letterhead-address">18 Harlow Avenue<br>New York, NY, 12345</address>
    <div class="brand-mark">Valtrix</div>
  </section>
</main>
</body>
</html>
```